VELOMIRA needs a label design for their product line of therapeutic CBD HEMP oil.

We are a company based out of Hawaii, USA called "VeloMira". We are needing a new look for our labels on our 2 oz bottles of CBD hemp oil. We are using organic CBD rich hemp oil and combining it with other organic oils to help heal inflammation, skin problems, and other ailments.

We have 6 different products of CBD oils :
x 2 CBD oil tinctures ( internal) : ZENITH CBD and BOTANIQ FORMULA
x 3 CBD skin care oils (external): CBD FACIAL SOLSTICE, CBD BODY
OIL, and CBD SKIN CARE
x 1 CBD Therapeutic oil ( external) SOOTHAVEX - Inflammation
Each product is in a 2 oz amber bottle with a black mist sprayer cap or black dropper and is a different color label. A green bottle ( zenith cbd), blue (botaniq), yellow(body oil), red/pink (restorative), purple( soothavex) the other colors???
I would like to use the color gold in our labels.

There is the logo for the name 'VeloMira", an oil droplet, and hemp leaf on each bottle.
I have the descriptive text/layout for the wording to be placed on the side of the bottles which just need a little font finessing.
I have designed the labels but just cannot seem to make them look professional and would like to re create the look.

I am seeking a label that looks professional for a successful business of high quality oils.

Target Market(s)

health food stores, alternative medicines, internet,

Industry/Entity Type

Graphic Design

Requirements
Must have
• I would like the word or logo for organic on the bottle.
• There must be a small space left for the bar code.
• I would like them all to look similar just with different colors and a slight different layout to distinguish the 2 internal CBD tiinctures ( CBD ZENTIH, BOTANIQ FORMULA) + soothavex from the 3 skin care external skin oils.
Nice to have
• I would like my product to have a hemp leaf somewhere on it but not too obvious.
• I am more concerned with the front design of the bottles than the written words on the sides of the bottle. That could be worked on later.
Should not have
• my label should not look too busy!

```html
<!DOCTYPE html>
<html lang="en">
<head>
<meta charset="utf-8">
<title>VeloMira CBD Label Line</title>
<link rel="stylesheet" href="https://fonts.googleapis.com/css2?family=Montserrat:wght@400;600;800&display=swap">
<style>
  :root {
    --bg-top: #f4f5f6;
    --bg-bottom: #d9dcdf;
    --label-white: #ffffff;
    --ink-dark: #3a3a3a;
    --leaf-green: #5fa83a;
    --leaf-green-light: #a5d37a;
    --blue: #1f5fc4;
    --purple: #8b2a9f;
    --orange: #f29100;
    --green: #38a63a;
  }
  * { box-sizing: border-box; margin: 0; padding: 0; }
  html, body { width: 900px; height: 1200px; overflow: hidden; }
  body {
    font-family: "Montserrat", sans-serif;
    background: linear-gradient(var(--bg-top), var(--bg-bottom));
    display: flex;
    align-items: center;
    justify-content: center;
  }
  .label-row {
    display: flex;
    gap: 20px;
  }
  .label {
    position: relative;
    width: 200px;
    height: 340px;
    background: var(--label-white);
    box-shadow: 0 6px 18px rgba(0,0,0,0.15);
    overflow: hidden;
    display: flex;
    flex-direction: column;
    align-items: center;
    text-align: center;
    padding-top: 24px;
  }
  .label--blue { --accent: var(--blue); }
  .label--purple { --accent: var(--purple); }
  .label--orange { --accent: var(--orange); }
  .label--green { --accent: var(--green); }

  .leaf-art {
    position: absolute;
    top: 0;
    left: 0;
    width: 110px;
    height: 46px;
    background: linear-gradient(135deg, var(--leaf-green), var(--leaf-green-light));
    border-bottom-right-radius: 46px;
  }
  .brand {
    position: relative;
    margin-top: 30px;
    display: flex;
    align-items: center;
    gap: 5px;
    font-size: 17px;
    font-weight: 600;
    color: var(--ink-dark);
  }
  .brand-dot {
    width: 9px;
    height: 9px;
    border-radius: 50%;
    background: var(--leaf-green);
  }
  .top-note {
    margin-top: 10px;
    font-size: 8px;
    line-height: 1.35;
    color: var(--accent);
  }
  .product-name {
    margin-top: 14px;
    padding: 0 12px;
    font-size: 19px;
    line-height: 1.1;
    font-weight: 800;
    letter-spacing: 0.3px;
    color: var(--accent);
  }
  .subtitle {
    margin-top: 6px;
    font-size: 8px;
    line-height: 1.35;
    color: var(--accent);
    text-transform: uppercase;
  }
  .band {
    position: absolute;
    left: 0;
    bottom: 0;
    width: 200px;
    height: 80px;
  }
  .band path { fill: var(--accent); }
  .band-text {
    position: absolute;
    left: 14px;
    bottom: 14px;
    font-size: 7px;
    color: var(--label-white);
  }
</style>
</head>
<body>
  <main class="label-row">
    <section class="label label--blue">
      <div class="leaf-art" role="img" aria-label="Hemp leaf illustration"></div>
      <div class="brand"><span class="brand-dot"></span>VeloMira</div>
      <p class="top-note">Organic Hemp<br>60ml · Full Spectrum</p>
      <h2 class="product-name">BOTANIQ FORMULA</h2>
      <svg class="band" viewBox="0 0 200 80" aria-hidden="true"><path d="M0 30 Q60 0 120 22 T200 20 V80 H0 Z"/></svg>
      <p class="band-text">2 fl oz · Hemp Supplement</p>
    </section>

    <section class="label label--purple">
      <div class="leaf-art" role="img" aria-label="Hemp leaf illustration"></div>
      <div class="brand"><span class="brand-dot"></span>VeloMira</div>
      <p class="top-note">Full Hemp Oil<br>CBD Rich Oil</p>
      <h2 class="product-name">SOOTHAVEX</h2>
      <p class="subtitle">Pure Herbal Organic Oils</p>
      <svg class="band" viewBox="0 0 200 80" aria-hidden="true"><path d="M0 30 Q60 0 120 22 T200 20 V80 H0 Z"/></svg>
      <p class="band-text">2 fl oz · Topical Use</p>
    </section>

    <section class="label label--orange">
      <div class="leaf-art" role="img" aria-label="Hemp leaf illustration"></div>
      <div class="brand"><span class="brand-dot"></span>VeloMira</div>
      <p class="top-note">Organic Blend</p>
      <h2 class="product-name">RECOVERY RITUAL OIL</h2>
      <p class="subtitle">With Organic Hemp Oil<br>&amp; CBD Rich Oil</p>
      <svg class="band" viewBox="0 0 200 80" aria-hidden="true"><path d="M0 30 Q60 0 120 22 T200 20 V80 H0 Z"/></svg>
      <p class="band-text">2 fl oz · Topical</p>
    </section>

    <section class="label label--green">
      <div class="leaf-art" role="img" aria-label="Hemp leaf illustration"></div>
      <div class="brand"><span class="brand-dot"></span>VeloMira</div>
      <p class="top-note">CBD Rich Hemp Oil<br>Organic Oil Extract</p>
      <h2 class="product-name">CBD ZENITH</h2>
      <svg class="band" viewBox="0 0 200 80" aria-hidden="true"><path d="M0 30 Q60 0 120 22 T200 20 V80 H0 Z"/></svg>
      <p class="band-text">2 fl oz · Hemp Supplement</p>
    </section>
  </main>
</body>
</html>
```